Pilates trainer needs new website

Summary: I need a new, meaningful website in a 1-page format, but one that can be expanded if necessary. I teach in various studios and in the future also in companies. Therefore, the website should convey growth, joy, uniqueness, workout and a bit of luxury.
The website should be inviting.
Layout:
Introduction what I offer
A bit about me
Option to upload price list and timetable in PDF format
Studio address where I teach
The color scheme should be petrol, gold, and colors that match. Not too dark, please.
My current website www.movewell-brennach.de, new domain is corebalance-studio.com (I have already purchased it)
Logo file attached
I have attached a few suggestions but I am also happy to be surprised.

Target Market(s)

Pilates private and small groups,

Industry/Entity Type

Pilates teacher freelancer

Coding

Coded - Design and coding required

Number of Pages Required

1 page

Requirements
Must have
• Welcoming appearance, about me, pictures, offers, colors from the logo but don't get do dark, more fresh and a bit luxurious
Should not have
• Not too wild and going crazy with colors

```html
<!DOCTYPE html>
<html lang="en">
<head>
<meta charset="utf-8">
<title>Lena Marwitz – Pilates Studio Trainer</title>
<link href="https://fonts.googleapis.com/css2?family=Prata&family=Poppins:wght@400;500&display=swap" rel="stylesheet">
<style>
:root{
  --teal:#14a89a;
  --teal-soft:#4fb3a5;
  --banner:#13a899;
  --ink:#1d1d1d;
  --text:#3b3b3b;
  --muted:#6b6b6b;
  --bg-soft:#f6f5f3;
  --white:#ffffff;
  --dots:#c9c9c9;
  --badge:#4b6a93;
  --gold:#a7b43a;
}
*{box-sizing:border-box;margin:0;padding:0}
html,body{width:1200px;height:3137px;overflow:hidden}
body{position:relative;background:var(--white);font-family:"Poppins",sans-serif;color:var(--text)}
.serif{font-family:"Prata",serif;font-weight:400;color:var(--ink)}
.abs{position:absolute}
.band{position:absolute;left:0;width:1200px}
.band-soft{background:var(--bg-soft)}
.center{text-align:center}
.pill{position:absolute;background:var(--teal-soft);color:#fff;border-radius:20px;font-size:14px;display:flex;align-items:center;justify-content:center}

/* nav */
.brand{position:absolute;left:113px;top:30px;display:flex;align-items:center;gap:10px;font-family:"Poppins",sans-serif;font-weight:500;font-size:17px;color:var(--teal)}
.brand .mark{width:14px;height:14px;border-radius:50%;background:var(--teal)}
.nav a{position:absolute;top:44px;font-size:15px;color:var(--teal);text-decoration:none}
.nav a.active{color:var(--ink);font-weight:500}
.nav .active-bar{position:absolute;left:330px;top:0;width:37px;height:3px;background:#555}

/* hero */
.eyebrow{left:184px;top:245px;font-size:14px;color:var(--teal);display:flex;align-items:center;gap:12px}
.eyebrow::before{content:"";width:36px;height:2px;background:#555}
.tagline{left:184px;top:276px;font-size:23px;line-height:28px;color:var(--teal)}
.hero-title{left:184px;top:344px;font-size:42px;line-height:45px}
.photo{position:absolute;border-radius:16px}
.dots{position:absolute;left:948px;top:491px}

/* intro */
.intro{left:215px;top:724px;width:770px;font-size:14.5px;line-height:19.5px;color:var(--text)}
.intro p+p{margin-top:19px}

/* about */
.about-title{left:618px;top:1040px;font-size:24px}
.about-text{left:618px;top:1083px;width:405px;font-size:14.5px;line-height:19.5px}

/* services */
.sec-title{left:0;width:1200px;font-size:24px;line-height:27px}
.sec-sub{left:0;width:1200px;font-size:14.5px;line-height:19.5px}
.card{position:absolute;width:252px;text-align:center}
.card.raised{background:#fff;border-radius:10px;box-shadow:0 6px 26px rgba(0,0,0,.08)}
.card h3{font-family:"Prata",serif;font-weight:400;font-size:15px;color:var(--ink)}
.card p{margin-top:24px;font-size:14.5px;line-height:19.5px;color:var(--text)}

/* pricing */
.col-title{font-size:24px;width:413px}
.plan-img{position:absolute;top:2051px;height:216px}
.plan-text{position:absolute;left:210px;top:2103px;width:365px;color:#fff;font-size:14.5px;line-height:19.5px;text-align:center}
.price-label{left:0;width:1200px;top:2354px;font-size:18px;font-weight:500;color:var(--teal)}

/* signup */
.banner{position:absolute;left:198px;top:2479px;width:803px;height:235px;background:var(--banner);border-radius:14px}
.banner h2{position:absolute;left:0;top:38px;width:803px;text-align:center;color:#fff;font-family:"Prata",serif;font-weight:400;font-size:31px;line-height:36px}
.signup{position:absolute;left:114px;top:149px;width:576px;height:42px;background:#fff;border-radius:21px;border:3px solid #fff}
.signup span{position:absolute;left:18px;top:10px;font-size:13.5px;color:#999}
.signup b{position:absolute;right:2px;top:2px;width:144px;height:32px;border-radius:16px;background:var(--teal);color:#fff;font-weight:500;font-size:14px;display:flex;align-items:center;justify-content:center}

/* footer */
.foot-brand{left:213px;top:2770px;display:flex;align-items:center;gap:8px;font-size:16px;font-weight:500;color:var(--teal)}
.foot-brand i{width:12px;height:12px;border-radius:50%;background:var(--teal);display:block}
.badge{position:absolute;left:199px;top:2839px;width:179px;height:216px;background:var(--badge);border-radius:6px}
.foot-name{left:351px;width:400px;top:2784px;font-size:23px}
.foot-info{left:351px;width:400px;font-size:14.5px;line-height:19.5px;color:var(--muted)}
.social{position:absolute;top:2999px;width:37px;height:37px;border-radius:50%;border:1.5px solid #222}
.social::after{content:"";position:absolute;left:13px;top:13px;width:8px;height:8px;border-radius:50%;background:#222}
.big-name{left:731px;top:2830px;width:268px;font-size:34px;line-height:44px;font-weight:500;color:var(--teal);text-align:center}
.copy{left:0;width:1200px;top:3097px;font-size:14.5px;color:var(--muted)}
.to-top{position:absolute;left:1087px;top:3087px;width:42px;height:42px;border-radius:50%;background:#111}
</style>
</head>
<body>

<!-- hero band -->
<div class="band band-soft" style="top:0;height:657px"></div>

<header class="nav">
  <div class="brand"><span class="mark"></span>MoveWell Brennach</div>
  <span class="active-bar"></span>
  <a class="active" style="left:331px">Home</a>
  <a style="left:419px">Individual training</a>
  <a style="left:593px">Group training</a>
  <a style="left:741px">About me</a>
  <a style="left:856px">Contact</a>
  <svg class="abs" style="left:975px;top:46px" width="16" height="16" viewBox="0 0 16 16" fill="none" stroke="#14a89a" stroke-width="2"><circle cx="7" cy="7" r="5"/><path d="M11 11l4 4"/></svg>
</header>

<section class="hero">
  <div class="abs eyebrow">Welcome to Pilates</div>
  <div class="abs tagline">Change happens through<br>movement and movement heals</div>
  <h1 class="abs serif hero-title">Lena Marwitz<br>Pilates Studio trainer</h1>
  <div class="pill" style="left:185px;top:460px;width:252px;height:30px">Request an Appointment Now</div>
  <svg class="dots" width="114" height="113" viewBox="0 0 114 113" aria-hidden="true">
    <defs><pattern id="dotgrid" width="10.2" height="10.2" patternUnits="userSpaceOnUse"><circle cx="3" cy="3" r="2.6" fill="#c9c9c9"/></pattern></defs>
    <rect x="62" y="0" width="52" height="113" fill="url(#dotgrid)"/>
    <rect x="0" y="71" width="114" height="42" fill="url(#dotgrid)"/>
  </svg>
  <div class="photo" role="img" aria-label="Portrait of the trainer smiling beside a wooden Pilates reformer tower" style="left:627px;top:150px;width:390px;height:409px;background:linear-gradient(135deg,#d9cdbd 0%,#a48a6c 45%,#2b2f45 100%)"></div>
</section>

<!-- intro -->
<div class="abs intro center">
  <p>The first prerequisite for being able to carry out our many different daily tasks with pleasure and joy is physical fitness, a consistently well-trained body and full possession of our mental powers.</p>
  <p>The comprehensive full-body training from Anton Kessler helps you achieve exactly this. The aim is to achieve optimal performance of the musculoskeletal system - strength, flexibility and endurance - without risk of injury. Anton Kessler originally called his method Contrology: The Art of Control. Contrology is the complete coordination of body, mind and spirit. The basic principles form the basis of all Pilates exercises with one goal: minimum effort - maximum success.</p>
</div>

<!-- about -->
<div class="band band-soft" style="top:945px;height:386px"></div>
<div class="photo" role="img" aria-label="Trainer performing a Pilates exercise on a reformer in the studio" style="left:175px;top:963px;width:399px;height:300px;border-radius:0 0 16px 16px;background:linear-gradient(160deg,#cdb48d 0%,#8f7a62 40%,#3a3f5a 80%,#b9b4ad 100%)"></div>
<h2 class="abs serif about-title">About Us</h2>
<p class="abs about-text">A technically excellent Pilates workout! Each training session includes new exercise sequences with precise instructions, and different small equipment is often used. My summary, definitely try it out, highly recommended. Thanks Lena!</p>
<div class="pill" style="left:618px;top:1207px;width:136px;height:29px">Learn More</div>

<!-- services -->
<h2 class="abs serif sec-title center" style="top:1390px">Revitalize Your Body with Expert<br>Pilates Training</h2>
<p class="abs sec-sub center" style="top:1457px">Discover the Power of Mindful Movement and Strengthen<br>Your Core with Our Certified Instructors."</p>

<div class="card" style="left:164px;top:1537px;height:219px">
  <svg width="50" height="54" viewBox="0 0 50 54" style="margin-top:17px" fill="none" stroke="#14a89a" stroke-width="1.8"><circle cx="25" cy="12" r="7"/><path d="M25 20v14M13 32l12-6 12 6M8 46h34l-6-10H14z"/><path d="M4 8h4M6 6v4M42 6h4M44 4v4"/></svg>
  <h3 style="margin-top:10px">Corporate Wellness:</h3>
  <p>Enrich your company's culture<br>with customized wellness<br>programs for employees.</p>
</div>
<div class="card raised" style="left:474px;top:1537px;height:219px">
  <svg width="66" height="48" viewBox="0 0 66 48" style="margin-top:24px" fill="none" stroke="#14a89a" stroke-width="1.8"><path d="M2 44h62"/><circle cx="54" cy="12" r="5"/><path d="M12 42l14-14 10 6 14-18M30 42l8-8"/></svg>
  <h3 style="margin-top:10px">Personalized Workouts:</h3>
  <p>Tailored fitness programs<br>designed to suit your unique<br>goals and lifestyle.</p>
</div>
<div class="card" style="left:780px;top:1537px;height:219px">
  <svg width="50" height="48" viewBox="0 0 50 48" style="margin-top:24px" fill="none" stroke="#14a89a" stroke-width="1.8"><path d="M6 18v14c0 6 4 10 10 10M16 14v14M44 18v14c0 6-4 10-10 10M34 14v14M21 6v18M25 4v20M29 6v18"/></svg>
  <h3 style="margin-top:10px">Group Classes:</h3>
  <p>Join our vibrant community<br>and experience the energy of<br>group workouts.</p>
</div>

<!-- pricing -->
<div class="band band-soft" style="top:1821px;height:582px"></div>
<h2 class="abs serif sec-title center" style="top:1857px">Convenient Access to Pricing and Timetables"</h2>
<p class="abs sec-sub center" style="top:1903px">"Stay Informed and Organized – Easily Upload and View<br>Our Price List and Timetable in PDF Format."</p>

<h3 class="abs serif col-title center" style="left:185px;top:1999px">Individual Training</h3>
<h3 class="abs serif col-title center" style="left:604px;top:1999px">Group Training</h3>

<div class="plan-img" role="img" aria-label="Dimmed photo of a one-to-one Pilates session on studio equipment" style="left:185px;width:413px;background:linear-gradient(135deg,#6d6a66 0%,#8c8882 50%,#55524f 100%)"></div>
<p class="plan-text">To get to know the Pilates method or because you don't have time to take part in group classes? Are you pursuing a specific training goal, have physical limitations or would you like to try Pilates for the first time as a beginner.<br>MORE</p>
<div class="plan-img" role="img" aria-label="Group of people sitting cross-legged meditating in a bright class" style="left:604px;width:413px;background:linear-gradient(135deg,#e6e4e2 0%,#b9b3ad 45%,#6a6a72 100%)"></div>

<svg class="abs" style="left:561px;top:2279px" width="76" height="76" viewBox="0 0 76 76" fill="none" stroke="#14a89a" stroke-width="3" aria-label="Download price list">
  <circle cx="38" cy="38" r="35"/>
  <path d="M38 22v24M28 37l10 10 10-10M24 46v8h28v-8"/>
</svg>
<div class="abs price-label center">price list</div>

<!-- signup -->
<div class="banner">
  <h2>Explore Our Services and Plan<br>Your Pilates Journey!</h2>
  <div class="signup"><span>Enter Your email address</span><b>Get Started</b></div>
</div>

<!-- footer -->
<div class="band band-soft" style="top:2714px;height:423px;z-index:-1"></div>
<div class="band band-soft" style="top:2701px;height:436px;z-index:-2"></div>
<div class="abs foot-brand"><i></i>MoveWell Brennach</div>
<div class="badge" aria-label="Association membership badge"></div>

<h2 class="abs serif foot-name center">Lena Marwitz</h2>
<p class="abs foot-info center" style="top:2840px">Pilates trainer</p>
<p class="abs foot-info center" style="top:2879px">Lindenweg 12<br>71234 Brennach</p>
<p class="abs foot-info center" style="top:2938px">phone +49 170 5550184<br>mail info@movewell-brennach.de</p>
<span class="social" style="left:484px"></span>
<span class="social" style="left:532px"></span>
<span class="social" style="left:579px"></span>

<div class="abs big-name">MoveWell<br>Brennach</div>

<p class="abs copy center">© Copyright Lena Marwitz | Pilates Glossary | Privacy Policy | imprint</p>
<div class="to-top">
  <svg width="42" height="42" viewBox="0 0 42 42" fill="none" stroke="#fff" stroke-width="1.6"><path d="M21 28V14M16 19l5-5 5 5"/></svg>
</div>

</body>
</html>
```